Optometrist/Eye Care Clinic Business card with new logo attached

We are a small, independent eye care clinic in Canada. We have recently updated our logo (as attached), and would like a professional, modern and health care oriented business card to highlight our office details and our optometrist. We'd like to incorporate the blue colours as seen on our logo.

Target Market(s)

demographic: age 35-65 male/female equal

Industry/Entity Type

Health Care

Contact Information for Business Card

Name of clinic: "Amber Hollow Eye Care Optometry"

Font styles to use
Sans Serif

Colors
0355a3

Requirements
Must have
• our website: amberholloweyecare.net
• Dr Selma Okonkwo
• Optometrist
• 312-617 E Larkspur Ave
• Vancouver BC V7R 3P8
• P: 604-555-0193
• E: info@amberholloweyecare.net
Nice to have
• front side: logo/name of clinic as seen on logo attached and website
• backside: logo on the left side, and name/title/address/phone/email

```html
<!DOCTYPE html>
<html lang="en">
<head>
<meta charset="utf-8">
<title>Amber Hollow Eye Care Optometry – Business Card</title>
<link rel="stylesheet" href="https://fonts.googleapis.com/css2?family=Open+Sans:wght@400;600&display=swap">
<style>
  :root {
    --backdrop: #3b3431;
    --card: #141516;
    --card-edge: #1d1f21;
    --brand-blue: #2a7fae;
    --brand-deep: #0355a3;
    --text-light: #e9ecee;
    --divider: #8a9096;
  }
  * { box-sizing: border-box; margin: 0; padding: 0; }
  html, body {
    width: 1200px; height: 864px; overflow: hidden;
    background: var(--backdrop);
    font-family: "Open Sans", Arial, sans-serif;
  }
  .stage {
    width: 1200px; height: 864px;
    display: flex; align-items: center; justify-content: center; gap: 48px;
  }
  .card {
    width: 540px; height: 309px;
    background: var(--card);
    border: 1px solid var(--card-edge);
    border-radius: 3px;
    box-shadow: 0 18px 40px rgba(0,0,0,.55);
    position: relative;
  }
  /* Front */
  .card--front {
    display: flex; flex-direction: column; align-items: center; justify-content: center; gap: 22px;
  }
  .brand-dot {
    width: 96px; height: 96px; border-radius: 50%;
    background: var(--brand-deep);
  }
  .brand-name {
    color: var(--brand-blue);
    font-weight: 400;
    text-align: center;
    letter-spacing: .14em;
    text-transform: uppercase;
    font-size: 19px;
    line-height: 1.35;
  }
  /* Back */
  .card--back {
    display: flex; align-items: center; padding: 0 34px 0 60px;
  }
  .card--back .brand-dot { width: 130px; height: 130px; flex: none; }
  .divider {
    width: 1px; height: 150px; background: var(--divider);
    margin: 0 26px 0 56px; flex: none;
  }
  .contact { color: var(--text-light); font-size: 13.5px; line-height: 1.45; }
  .contact__name { color: var(--brand-blue); font-size: 17px; font-weight: 400; }
  .contact__title { color: var(--brand-blue); font-size: 13.5px; font-weight: 600; margin-bottom: 8px; }
  .contact__row { display: flex; align-items: center; gap: 8px; }
  .contact__row svg { width: 11px; height: 11px; flex: none; fill: var(--brand-blue); }
</style>
</head>
<body>
  <main class="stage">
    <section class="card card--front" aria-label="Card front">
      <div class="brand-dot"></div>
      <p class="brand-name">Amber Hollow<br>Eye Care<br>Optometry</p>
    </section>

    <section class="card card--back" aria-label="Card back">
      <div class="brand-dot" aria-hidden="true"></div>
      <div class="divider"></div>
      <div class="contact">
        <p class="contact__name">Dr Selma Okonkwo</p>
        <p class="contact__title">Optometrist</p>
        <p>312-617 E Larkspur Ave</p>
        <p style="margin-bottom:4px">Vancouver BC V7R 3P8</p>
        <p class="contact__row">
          <svg viewBox="0 0 24 24" aria-label="Phone"><path d="M6.6 10.8a15.1 15.1 0 0 0 6.6 6.6l2.2-2.2a1 1 0 0 1 1-.25 11.4 11.4 0 0 0 3.6.57 1 1 0 0 1 1 1V20a1 1 0 0 1-1 1A17 17 0 0 1 3 4a1 1 0 0 1 1-1h3.5a1 1 0 0 1 1 1c0 1.25.2 2.45.57 3.6a1 1 0 0 1-.25 1z"/></svg>
          604-555-0193
        </p>
        <p class="contact__row">
          <svg viewBox="0 0 24 24" aria-label="Email"><path d="M2 5h20v14H2zm2 2v.4l8 5 8-5V7z"/></svg>
          info@amberholloweyecare.net
        </p>
        <p class="contact__row">
          <svg viewBox="0 0 24 24" aria-label="Website"><circle cx="12" cy="12" r="10"/></svg>
          www.amberholloweyecare.net
        </p>
      </div>
    </section>
  </main>
</body>
</html>
```